EPS Recycling Rpt

Our annual recycling rate report needs a tune up. Our organization helps faciltate expanded polystyrene (EPS) recycling and this 4-page report highlights growth trends and useful information to help readers understand the dynamics of EPS recycling. We need a designer that can recreate the brochure we've published over the past several years with some minor adjustments to accomodate new content.

A PDF of the 2012 report is attached. Header text should reflect 2013 in all cases. Please pay close attention to the new placement of the copy as indicated in the Word file (also attached) as it has been significantly modified from the 2012 version. The color pallette for our branding is provided. Contact us with any questions.

```html
<!DOCTYPE html>
<html lang="en">
<head>
<meta charset="utf-8">
<title>EPS Recycling: Stronger Than Ever</title>
<link href="https://fonts.googleapis.com/css2?family=Oswald:wght@500&family=Roboto+Condensed:wght@300;400;700&display=swap" rel="stylesheet">
<style>
  :root {
    --orange: #f7941d;
    --orange-deep: #f26522;
    --blue: #2b7cb3;
    --ink: #3a3a3a;
    --grid: #d9d9d9;
    --axis: #8a8a8a;
    --paper: #ffffff;
    --foam-green: #b9dba8;
    --foam-white: #eef3ec;
  }
  html, body { margin: 0; padding: 0; overflow: hidden; }
  body { width: 927px; height: 1200px; background: var(--paper); position: relative; font-family: "Roboto Condensed", "Arial Narrow", sans-serif; color: var(--ink); }
  .hero-photo {
    position: absolute; left: 0; top: 0; width: 927px; height: 362px;
    background:
      radial-gradient(circle at 20% 30%, rgba(255,255,255,.7) 0, transparent 18%),
      radial-gradient(circle at 65% 55%, rgba(255,255,255,.6) 0, transparent 20%),
      radial-gradient(circle at 85% 20%, rgba(255,255,255,.6) 0, transparent 16%),
      linear-gradient(160deg, var(--foam-white) 0%, var(--foam-green) 45%, var(--foam-white) 75%, var(--foam-green) 100%);
  }
  .title-band { position: absolute; left: 0; top: 331px; width: 590px; height: 80px; }
  .title-band svg { position: absolute; inset: 0; }
  .title-band h1 {
    position: relative; margin: 0; padding: 26px 0 0 14px;
    font-family: "Oswald", "Arial Narrow", sans-serif; font-weight: 500;
    font-size: 33px; line-height: 1; color: #fff; letter-spacing: .2px;
  }
  p { margin: 0; font-size: 9.6px; line-height: 12.6px; font-weight: 400; }
  .intro { position: absolute; left: 57px; top: 437px; width: 814px; }
  h2 {
    margin: 0; font-family: "Oswald", "Arial Narrow", sans-serif; font-weight: 500;
    color: var(--blue); font-size: 19px; line-height: 1; text-transform: uppercase;
  }
  .figure-title { position: absolute; left: 57px; top: 496px; }
  .chart { position: absolute; left: 0; top: 540px; }
  .chart text { font-family: "Roboto Condensed", sans-serif; font-weight: 700; font-size: 16px; fill: var(--axis); }
  .methodology { position: absolute; left: 57px; top: 788px; width: 814px; }
  .criteria { position: absolute; left: 57px; top: 998px; width: 814px; }
  .section h2 { margin-bottom: 11px; }
  .section p + p { margin-top: 0; }
  .section p.spaced { margin-top: 11px; }
</style>
</head>
<body>
  <div class="hero-photo" role="img" aria-label="Close-up photo of green and white foam packing peanuts"></div>

  <header class="title-band">
    <svg width="590" height="80" viewBox="0 0 590 80" aria-hidden="true">
      <defs>
        <linearGradient id="bandFill" x1="0" x2="1">
          <stop offset="0" stop-color="var(--orange)"/>
          <stop offset="1" stop-color="var(--orange-deep)"/>
        </linearGradient>
      </defs>
      <polygon points="0,0 590,0 544,80 0,80" fill="url(#bandFill)"/>
    </svg>
    <h1>EPS RECYCLING: STRONGER THAN EVER</h1>
  </header>

  <p class="intro">As shown in Figure 2, the EPS packaging recycling rate percentage continues to grow steadily, showing a dependable track record to deliver consistent results. In fact, when comparing rigid, durable PS and other grade materials, EPS post-consumer and post-commercial recycling represent 47% of all post-use polystyrene recycled in the U.S. and is one of the highest within the plastics family.</p>

  <h2 class="figure-title">Figure 2: Post-Consumer EPS Recycling Rate History (1990-2013)</h2>

  <svg class="chart" width="927" height="215" viewBox="0 540 927 215" role="img" aria-label="Line chart of post-consumer EPS recycling rate from about 2% in 1990 to about 34% in 2013">
    <g stroke="var(--grid)" stroke-width="2">
      <line x1="82" y1="556" x2="840" y2="556"/>
      <line x1="82" y1="595" x2="840" y2="595"/>
      <line x1="82" y1="633" x2="840" y2="633"/>
      <line x1="82" y1="672" x2="840" y2="672"/>
      <line x1="82" y1="711" x2="840" y2="711"/>
    </g>
    <g text-anchor="start">
      <text x="48" y="562">40</text>
      <text x="48" y="601">30</text>
      <text x="48" y="639">20</text>
      <text x="48" y="678">10</text>
      <text x="56" y="717">0</text>
    </g>
    <polyline fill="none" stroke="var(--orange)" stroke-width="3" stroke-linejoin="round"
      points="113,701 170,674 226,670 283,670 340,673 396,664 453,661 509,664 566,635 623,635 679,602 736,595 831,579"/>
    <g fill="var(--orange)">
      <circle cx="113" cy="701" r="8"/><circle cx="170" cy="674" r="8"/><circle cx="226" cy="670" r="8"/>
      <circle cx="283" cy="670" r="8"/><circle cx="340" cy="673" r="8"/><circle cx="396" cy="664" r="8"/>
      <circle cx="453" cy="661" r="8"/><circle cx="509" cy="664" r="8"/><circle cx="566" cy="635" r="8"/>
      <circle cx="623" cy="635" r="8"/><circle cx="679" cy="602" r="8"/><circle cx="736" cy="595" r="8"/>
      <circle cx="831" cy="579" r="8"/>
    </g>
    <g text-anchor="middle">
      <text x="113" y="742">1990</text><text x="170" y="742">1992</text><text x="226" y="742">1994</text>
      <text x="283" y="742">1996</text><text x="340" y="742">1998</text><text x="396" y="742">2000</text>
      <text x="453" y="742">2002</text><text x="509" y="742">2004</text><text x="566" y="742">2006</text>
      <text x="623" y="742">2008</text><text x="679" y="742">2010</text><text x="736" y="742">2012</text>
      <text x="831" y="742">2013</text>
    </g>
  </svg>

  <section class="section methodology">
    <h2>Report Methodology</h2>
    <p>The methodology for this annual report focuses on the development of a numerator and denominator figure. Recycled pounds, used as the numerator in the recycling rate equation, are based on an annual survey of post-consumer and post-commercial plastic recyclers (including EPS industry manufacturing facilities ) and reflect the quantity of EPS recycled each year. Recycled pounds were counted at the stage where materials enter a reclamation facility (as opposed to net material recycled into resin or products) or were shipped for recycling outside the U.S.</p>
    <p>Due to supply distribution chains and multiple end-use applications for EPS, a fixed number for EPS packaging generated each year is not available. Other manufacturing streams include building and construction applications, sporting goods and other durable products. As a proxy, resin sales data as reported for custom moded applications are used as the denominator in the recycling rate equations, which were provided by the National Resin Council (NRC) Plastics Industry Producers' Statistics Group. NRC reports are compiled from primary data reported by resin producers to the professional services firm of Harlow Analytics, LLC. This does not account for non-U.S. resin sales which may offset the quantities reported by U.S. resin suppliers sold into custom molding facilities for non-packaging applications.</p>
  </section>

  <section class="section criteria">
    <h2>Recycling Criteria</h2>
    <p>Not all materials are well suited for recycling. Post-consumer EPS packaging must be clean and free of tape, film and cardboard. Expanded polystyrene made with a fire retardant additive, typically used in the manufacture of EPS building insulation, requires special reprocessing conditions. To enhance collection efforts and maximize the investment in recycling equipment, FPC recycling locations concentrate on large volume, commercial sources of post-consumer EPS. Some locations also offer consumer drop-off access.</p>
    <p class="spaced">To find out if EPS recycling is available in your area, visit www.foamrecyclecouncil.example. For consumers that do not have access to a local drop-off center, the Coalition of Foam Recyclers sponsors a National Take-Back Program intended for smaller quantities of EPS which can be mailed via national mail or ParcelWay to more than 30 locations nationwide. Full instructions and a list of Take-Back locations are available on the FPC website</p>
  </section>
</body>
</html>
```